Skin Care Product Line needs custom designed labels

We need one to two label design templates that can be used across our natural skin care products such as body lotion, salt scrubs, lip balms, handmade soaps, body creams, body mists, foot creams, bath salts. The design will come in different colors. We have our own logo; however the logo should have the flower colored golden along with the word tavin.
Label sizes are :
1) 6 inches by 4 inches rectangular for body lotion,
2) 81/2 inches by 2 inches rectangular for body scrub,
3) 5 inches by 3 inches rectangular for body mist,
4) 2 inches by 3 inches for bath salts,
5) 2.125 inches by 2.125 inches for lip balm,
6) 11/2 inches by 1/12 inches label for soap.
Updates

The design should have a beige background with one color or two of the same colors for instance light lavender and a darker lavender. It should have a vintage feel to it because it's for a natural skin care line not commercial type. Also the fonts should be vintage looking. We can have one design with different colors such as light green, light yellow, light pink, light blue , light orange to go with the different scents. Added Tuesday, January 26, 2016

Target Market(s)

Young adults and aging boomers

Industry/Entity Type

Skin Care Product

Font styles to use
Decorative

Colors
cfeae6
b7a5cd
e4daeb
fbf289
fac994
9bcb3b
f9d9e8
f04a50
f68d4c

Requirements
Must have
• Please see attached image for design sample. Original Label design should have beige to tan colored background similar to the attached file. light colors such as lavender, light yellow, light orange, etc can be changed once original label is designed. We would need to be able to edit label design text and label design colors to match our different scents after we decide on the design.

```html
<!DOCTYPE html>
<html lang="en">
<head>
<meta charset="utf-8">
<title>Velora tavin — Bath Salts Labels</title>
<link rel="stylesheet" href="https://fonts.googleapis.com/css2?family=IM+Fell+English&family=Kurale&display=swap">
<style>
  :root {
    --page: #ffffff;
    --brown: #4a3a26;
    --gold: #b8955a;
    --gold-mark: #e8b732;
    --ribbon-text: #f6efe0;
    --cream: #f7f1e1;
    --lavender: #e4daeb;
    --mint: #cfeae6;
  }
  * { box-sizing: border-box; margin: 0; padding: 0; }
  html, body {
    width: 1200px; height: 493px; overflow: hidden;
    background: var(--page);
  }
  .label-set { position: relative; width: 1200px; height: 493px; }
  .label {
    position: absolute; top: 62px; width: 360px; height: 370px;
    overflow: hidden;
  }
  .label--unscented { left: 25px; background: var(--cream); }
  .label--lavender  { left: 420px; background: var(--lavender); }
  .label--peppermint{ left: 815px; background: var(--mint); }

  .flourish {
    position: absolute; width: 78px; height: 340px; top: 15px;
    background: linear-gradient(180deg, rgba(184,149,90,.35), rgba(184,149,90,.12) 45%, rgba(184,149,90,.35));
    border-radius: 6px;
  }
  .flourish--left { left: 8px; }
  .flourish--right { right: 8px; }

  .brand {
    position: absolute; top: 92px; left: 0; right: 0;
    display: flex; justify-content: center; align-items: center; gap: 8px;
    font-family: "IM Fell English", serif; font-size: 24px;
    color: var(--brown); letter-spacing: .5px;
  }
  .brand-dot {
    width: 14px; height: 14px; border-radius: 50%; background: var(--gold-mark);
  }
  .product-name {
    position: absolute; top: 178px; left: 0; right: 0; text-align: center;
    font-family: "Kurale", serif; font-size: 50px; color: var(--brown);
    line-height: 1;
  }
  .scent-ribbon {
    position: absolute; top: 258px; left: 50%; transform: translateX(-50%);
    width: 230px; height: 34px;
  }
  .scent-ribbon svg { position: absolute; inset: 0; }
  .scent-name {
    position: relative; display: block; text-align: center; line-height: 34px;
    font-family: "IM Fell English", serif; font-size: 21px; color: var(--ribbon-text);
  }
  .net-weight {
    position: absolute; top: 330px; left: 0; right: 0; text-align: center;
    font-family: "IM Fell English", serif; font-size: 15px; color: var(--brown);
  }
</style>
</head>
<body>
<main class="label-set">

  <section class="label label--unscented">
    <div class="flourish flourish--left" role="img" aria-label="Vintage gold floral scroll ornament"></div>
    <div class="flourish flourish--right" role="img" aria-label="Vintage gold floral scroll ornament"></div>
    <div class="brand"><span class="brand-dot"></span>Velora tavin</div>
    <h2 class="product-name">Bath Salts</h2>
    <div class="scent-ribbon">
      <svg viewBox="0 0 230 34" preserveAspectRatio="none"><polygon points="0,0 230,0 220,17 230,34 0,34 10,17" fill="var(--brown)"/></svg>
      <span class="scent-name">Aroma name</span>
    </div>
    <p class="net-weight">4oz/100g</p>
  </section>

  <section class="label label--lavender">
    <div class="flourish flourish--left" role="img" aria-label="Vintage gold floral scroll ornament"></div>
    <div class="flourish flourish--right" role="img" aria-label="Vintage gold floral scroll ornament"></div>
    <div class="brand"><span class="brand-dot"></span>Velora tavin</div>
    <h2 class="product-name">Bath Salts</h2>
    <div class="scent-ribbon">
      <svg viewBox="0 0 230 34" preserveAspectRatio="none"><polygon points="0,0 230,0 220,17 230,34 0,34 10,17" fill="var(--brown)"/></svg>
      <span class="scent-name">Lavender</span>
    </div>
    <p class="net-weight">4oz/100g</p>
  </section>

  <section class="label label--peppermint">
    <div class="flourish flourish--left" role="img" aria-label="Vintage gold floral scroll ornament"></div>
    <div class="flourish flourish--right" role="img" aria-label="Vintage gold floral scroll ornament"></div>
    <div class="brand"><span class="brand-dot"></span>Velora tavin</div>
    <h2 class="product-name">Bath Salts</h2>
    <div class="scent-ribbon">
      <svg viewBox="0 0 230 34" preserveAspectRatio="none"><polygon points="0,0 230,0 220,17 230,34 0,34 10,17" fill="var(--brown)"/></svg>
      <span class="scent-name">Peppermint</span>
    </div>
    <p class="net-weight">4oz/100g</p>
  </section>

</main>
</body>
</html>
```